Vertical Banner

I need an eye-catching banner created for street fairs, indoor and outdoor events to draw attention to our language school. It will be to print on this banner (specs included):
https://www.plivorasupply.com/tag/617/Retractable-Banners/product/5173-48/Basic-Rollup-Banner-Stand-29-14

I want the banner to be:
- SIMPLE
- Eye catching (not busy with too many pictures or information)
- It should say at top prominently: "Come learn a language!" and have our name.
- Below these languages should be large and eye-catching: Spanish, Chinese, French, Russian, German, Italian, Farsi, Turkish, Portuguese, ASL, Cantonese, Japanese, Korean, Vietnamese, Arabic, Dutch, more... (if some need to be cut our because of overcrowding let me know OR we can make some big and others small)
- Below this it should have GROUP & PRIVATE LESSONS
- It should be colorful and make people think of things international - perhaps national flags in background? Or images of world famous monuments? Could be image of adutls in a classroom. Sth that gets people excited about travel and language learning
- It should have our contact info VERY large at bottom:
Quill Languages -
San Francisco, Silicon Valley & New York City
www.quilllanguagesf.com
415-962-4051
info@quilllanguagesf.com
(this can be smaller)
Four Halvorsen Plaza
Lobby 3
San Francisco, CA 94127

Hey Designers, please feel free to do a rough take on it. I don't need you to spend too much time, just give me a general idea of how you would make it look, then i know we can go from there later and refine it. Feel free to make it more of a quick sketch to show how you would do it.

Target Market(s)

adults from about 25-55 years old, educated, employed and typically world travellers

Industry/Entity Type

School

Colors
86cfc6
00a990
cadf82
acd036
9bcb3c
fbed22
f78f20
ffc214
f37122

Requirements
Must have
• Must be simple! Too many banners put way too much information and pictures. I want someone to walk by and immediately know we teach foreign languages. Must have bright colors and large font for languages offered
Should not have
• Should not be too full of images and design that distract the viewer from seeing the main thing I want them to see: that we teacher languages

```html
<!DOCTYPE html>
<html lang="en">
<head>
<meta charset="utf-8">
<title>Quill Languages – Roll-up Banner</title>
<link rel="stylesheet" href="https://fonts.googleapis.com/css2?family=Anton&family=Lobster&family=Roboto+Condensed:wght@400;700&display=swap">
<style>
  :root {
    --page-bg: #d9dadc;
    --white: #ffffff;
    --brand-green: #0a8a3a;
    --banner-red: #e30613;
    --headline-yellow: #ffe600;
    --ink: #111111;
    --cloud-light: #f4f4f4;
    --cloud-mid: #e4e4e4;
  }
  * { box-sizing: border-box; margin: 0; padding: 0; }
  html, body {
    width: 1200px; height: 1175px; overflow: hidden;
    background: var(--page-bg);
  }
  .banner {
    position: absolute; left: 385px; top: 20px;
    width: 430px; height: 1135px;
    background: var(--white);
    overflow: hidden;
    box-shadow: 0 6px 24px rgba(0,0,0,.18);
  }
  .brand {
    position: absolute; top: 0; left: 0; width: 100%; height: 213px;
    display: flex; align-items: center; justify-content: center;
  }
  .brand-name {
    font-family: "Roboto Condensed", Arial, sans-serif;
    font-weight: 700; font-size: 58px; color: var(--brand-green);
    letter-spacing: -0.5px;
  }
  .headline-band {
    position: absolute; top: 200px; left: 0; width: 100%; height: 215px;
  }
  .headline-band svg { position: absolute; inset: 0; }
  .headline {
    position: absolute; top: 30px; left: 0; width: 100%;
    font-family: "Anton", Impact, sans-serif; color: var(--headline-yellow);
    text-align: center; line-height: 0.98; text-transform: uppercase;
  }
  .headline .line-1 { display: block; font-size: 68px; }
  .headline .line-2 { display: block; font-size: 92px; }
  .greeting-cloud {
    position: absolute; top: 415px; left: 0; width: 100%; height: 196px;
    background: linear-gradient(180deg, var(--cloud-mid), var(--cloud-light) 60%, var(--white));
  }
  .learners-photo {
    position: absolute; top: 611px; left: 12px; width: 406px; height: 84px;
    background: linear-gradient(90deg, #f1a24a, #e7c9a8 30%, #f0e27a 50%, #5b78b8 70%, #e9c4a0);
  }
  .language-panel {
    position: absolute; top: 695px; left: 14px; width: 402px; height: 230px;
    background: var(--brand-green);
    padding-top: 14px;
    font-family: "Roboto Condensed", Arial, sans-serif; font-weight: 700;
    color: var(--white); font-size: 24px; line-height: 36px; text-align: center;
  }
  .language-panel .sep { color: var(--headline-yellow); padding: 0 5px; font-weight: 400; }
  .lessons-ribbon {
    position: absolute; top: 905px; left: 0; width: 100%; height: 62px;
  }
  .lessons-ribbon svg { position: absolute; inset: 0; }
  .lessons-ribbon span {
    position: absolute; inset: 0; display: flex; align-items: center; justify-content: center;
    padding-top: 4px;
    font-family: "Lobster", cursive; font-size: 30px; color: var(--headline-yellow);
  }
  .contact {
    position: absolute; top: 972px; left: 0; width: 100%;
    font-family: "Roboto Condensed", Arial, sans-serif; font-weight: 700;
    color: var(--ink); text-align: center;
  }
  .contact .regions { font-size: 17px; line-height: 21px; }
  .contact .row { font-size: 16px; line-height: 21px; display: flex; justify-content: center; align-items: center; gap: 6px; }
  .contact .row.small { font-size: 14px; font-weight: 400; }
  .contact .icon { width: 13px; height: 13px; }
  .contact .address { font-size: 18px; line-height: 21px; margin-top: 3px; }
  .base-band { position: absolute; left: 0; bottom: 0; width: 100%; height: 48px; }
</style>
</head>
<body>
<div class="banner">
  <header class="brand">
    <span class="brand-name">Quill Languages</span>
  </header>

  <section class="headline-band">
    <svg width="430" height="215" viewBox="0 0 430 215" aria-hidden="true">
      <path d="M0 12 Q215 36 430 22 L430 215 L0 215 Z" fill="var(--banner-red)"/>
      <path d="M0 12 Q215 36 430 22 L430 30 Q215 44 0 20 Z" fill="var(--headline-yellow)"/>
    </svg>
    <h1 class="headline">
      <span class="line-1">Come learn a</span>
      <span class="line-2">Language!</span>
    </h1>
  </section>

  <div class="greeting-cloud" role="img" aria-label="Faint word cloud of greetings such as hello, bonjour and ciao in many languages and scripts"></div>
  <div class="learners-photo" role="img" aria-label="Photo of five smiling young adults looking upward over the language panel"></div>

  <section class="language-panel">
    <div>Spanish<span class="sep">|</span>Chinese<span class="sep">|</span>French<span class="sep">|</span>Russian</div>
    <div>German<span class="sep">|</span>Italian<span class="sep">|</span>Farsi<span class="sep">|</span>Turkish<span class="sep">|</span>ASL</div>
    <div>Portuguese<span class="sep">|</span>Cantonese<span class="sep">|</span>Japanese</div>
    <div>Korean<span class="sep">|</span>Arabic<span class="sep">|</span>Dutch</div>
    <div>Vietnamese<span class="sep">|</span>more...</div>
  </section>

  <div class="lessons-ribbon">
    <svg width="430" height="62" viewBox="0 0 430 62" aria-hidden="true">
      <path d="M14 14 L416 6 L404 32 L416 56 L14 56 L26 34 Z" fill="var(--banner-red)"/>
    </svg>
    <span>Group &amp; Private Lessons</span>
  </div>

  <section class="contact">
    <p class="regions">San Francisco, Silicon Valley &amp; New York City</p>
    <p class="row">
      <svg class="icon" viewBox="0 0 16 16" aria-hidden="true"><circle cx="8" cy="8" r="8" fill="var(--ink)"/><path d="M5 4 L7 4 L7.5 6.5 L6.5 7.3 Q7.5 9 9 9.6 L9.8 8.6 L12 9 L12 11 Q8 12 5 8 Q4 6 5 4 Z" fill="#fff"/></svg>
      415-962-4051
      <svg class="icon" viewBox="0 0 16 16" aria-hidden="true" style="margin-left:8px"><circle cx="8" cy="8" r="7" fill="none" stroke="var(--ink)" stroke-width="1.4"/><ellipse cx="8" cy="8" rx="3" ry="7" fill="none" stroke="var(--ink)" stroke-width="1.2"/><line x1="1" y1="8" x2="15" y2="8" stroke="var(--ink)" stroke-width="1.2"/></svg>
      www.quilllanguagesf.com
    </p>
    <p class="row small">
      <svg class="icon" viewBox="0 0 16 16" aria-hidden="true"><rect x="1.5" y="3.5" width="13" height="9" fill="none" stroke="var(--ink)" stroke-width="1.4"/><path d="M1.5 3.5 L8 9 L14.5 3.5" fill="none" stroke="var(--ink)" stroke-width="1.4"/></svg>
      info@quilllanguagesf.com
    </p>
    <p class="address">Four Halvorsen Plaza, Lobby 3<br>San Francisco, CA 94127</p>
  </section>

  <svg class="base-band" width="430" height="48" viewBox="0 0 430 48" aria-hidden="true">
    <path d="M0 30 Q215 20 430 2 L430 48 L0 48 Z" fill="var(--brand-green)"/>
  </svg>
</div>
</body>
</html>
```